Park Company Mobile Application Design

We are looking for deisgn of the mobile application for the parking company. More details about the parking company you can find on the following web site: www.tvr.mk.
As well we attached the parking card that this company is issuing. As you may see their preferred color is green.
Attached you can find screens that we are planning to implement in the mobile application.
If you need more details please contact us on goran@brelo.mk.

Thanks,
Goran Dimovski
Brelo Group

```html
<!DOCTYPE html>
<html lang="en">
<head>
<meta charset="utf-8">
<title>Parkovo – Mobile App Screens</title>
<link href="https://fonts.googleapis.com/css2?family=Roboto:wght@400;500;700&display=swap" rel="stylesheet">
<style>
  :root {
    --green: #52b848;
    --wave-teal: #b5e0d3;
    --wave-soft: #c9e8c3;
    --field-border: #d4d4d4;
    --placeholder: #a9a9a9;
    --dot: #bdbdbd;
    --ink: #333333;
    --canvas: #e7e7e7;
    --white: #ffffff;
  }
  * { box-sizing: border-box; margin: 0; padding: 0; }
  html, body { width: 1105px; height: 1200px; overflow: hidden; }
  body {
    background: var(--canvas);
    font-family: "Roboto", sans-serif;
    position: relative;
  }
  .screen {
    position: absolute;
    width: 307px;
    height: 545px;
    background: var(--white);
    overflow: hidden;
  }
  .header { position: absolute; left: 0; top: 0; width: 307px; height: 74px; }
  .header svg { position: absolute; left: 0; top: 0; display: block; }
  .header--tall { height: 112px; }
  .status-bar {
    position: absolute; left: 0; top: 0; width: 307px; height: 30px;
    color: var(--white); font-size: 13px;
  }
  .status-bar .signal { position: absolute; left: 18px; top: 9px; }
  .status-bar .time { position: absolute; left: 0; width: 307px; top: 8px; text-align: center; }
  .status-bar .power { position: absolute; right: 14px; top: 8px; display: flex; align-items: center; gap: 4px; }
  .brand {
    position: absolute; left: 0; width: 307px;
    display: flex; align-items: center; justify-content: center; gap: 8px;
    color: var(--green); font-weight: 700; font-size: 30px; letter-spacing: 0.5px;
  }
  .brand .brand-dot { width: 22px; height: 22px; border-radius: 50%; background: var(--green); }
  .field {
    position: absolute; left: 38px; width: 231px; height: 39px;
    border: 1.5px solid var(--field-border); border-radius: 20px;
    display: flex; align-items: center; padding-left: 20px;
    color: var(--placeholder); font-size: 13.5px;
  }
  .field--icon { padding-left: 16px; gap: 10px; }
  .field--indent { padding-left: 44px; }
  .btn {
    position: absolute; left: 65px; width: 177px; height: 39px;
    background: var(--green); border-radius: 20px; color: var(--white);
    display: flex; align-items: center; justify-content: center;
    font-size: 13px; font-weight: 500;
  }
  .btn--small { font-size: 9.5px; }
  .btn--bold { font-weight: 700; }
  .options-row {
    position: absolute; left: 0; width: 307px; top: 353px;
    font-size: 5.5px; color: var(--ink);
  }
  .options-row .remember { position: absolute; left: 78px; top: 0; display: flex; align-items: center; gap: 3px; }
  .options-row .forgot { position: absolute; left: 179px; top: 1px; color: #888; }
  .signup-line {
    position: absolute; top: 474px; left: 0; width: 307px; text-align: center;
    font-size: 10.5px; color: #666;
  }
  .signup-line strong { color: var(--green); font-weight: 700; margin-left: 6px; }
  .choice {
    position: absolute; left: 59px; display: flex; align-items: center; gap: 16px;
    font-size: 12.5px; color: var(--ink);
  }
  .choice--active { color: var(--green); }
  .choice .box { width: 12px; height: 12px; border: 1px solid #bbb; border-radius: 2px; }
  .pager { position: absolute; left: 0; width: 307px; display: flex; justify-content: center; gap: 7px; }
  .pager span { width: 7px; height: 7px; border-radius: 50%; background: var(--dot); }
  .pager span.active { width: 9px; height: 9px; background: var(--green); margin-top: -1px; }
  .menu-icon { position: absolute; left: 18px; top: 50px; }
  .page-title { position: absolute; right: 15px; top: 58px; color: var(--white); font-size: 13.5px; font-weight: 500; }
  .tab-bar {
    position: absolute; left: 0; bottom: 0; width: 307px; height: 49px; background: var(--green);
    display: flex; color: var(--white); font-size: 6.5px; font-weight: 700;
  }
  .tab-bar .tab {
    flex: 1; display: flex; flex-direction: column; align-items: center; justify-content: flex-end;
    padding-bottom: 8px; gap: 4px; position: relative;
  }
  .tab-bar .tab--current::after {
    content: ""; position: absolute; bottom: 3px; width: 32px; height: 1.5px; background: var(--white);
  }
</style>
</head>
<body>

<svg width="0" height="0" style="position:absolute">
  <defs>
    <g id="wave">
      <path d="M0 62 C20 67 40 69 58 69 C38 73 16 73 0 70 Z" fill="var(--wave-soft)"/>
      <path d="M0 0 H307 V63 C300 64 290 65 275 64 C240 60 200 45 165 45 C140 46 125 52 100 60 C70 70 30 70 0 62 Z" fill="var(--green)"/>
      <path d="M140 48 C160 40 180 38 200 42 C220 46 235 52 250 57 C225 52 190 47 140 48 Z" fill="var(--wave-teal)"/>
    </g>
    <g id="status-signal" fill="#fff">
      <rect x="0" y="6" width="2.5" height="4"/>
      <rect x="4" y="4" width="2.5" height="6"/>
      <rect x="8" y="2" width="2.5" height="8"/>
      <rect x="12" y="0" width="2.5" height="10"/>
      <path d="M20 3 Q27 -2 34 3" stroke="#fff" stroke-width="1.6" fill="none"/>
      <path d="M22.5 5.5 Q27 2 31.5 5.5" stroke="#fff" stroke-width="1.6" fill="none"/>
      <circle cx="27" cy="8.5" r="1.5"/>
    </g>
    <g id="bluetooth">
      <path d="M1 3.5 L7 9 L4 11.5 V0.5 L7 3 L1 8.5" stroke="#fff" stroke-width="1.1" fill="none"/>
    </g>
    <g id="battery">
      <rect x="0.5" y="0.5" width="26" height="12" rx="2" fill="none" stroke="#fff"/>
      <rect x="2.5" y="2.5" width="22" height="8" rx="1" fill="#fff"/>
      <rect x="27.5" y="4" width="2" height="5" fill="#fff"/>
    </g>
  </defs>
</svg>

<!-- Sign in -->
<section class="screen" style="left:39px;top:24px">
  <div class="header"><svg width="307" height="74" viewBox="0 0 307 74"><use href="#wave"/></svg></div>
  <div class="status-bar">
    <svg class="signal" width="36" height="11"><use href="#status-signal"/></svg>
    <div class="time">10:30 AM</div>
    <div class="power"><svg width="8" height="12"><use href="#bluetooth"/></svg><span>100%</span><svg width="30" height="13"><use href="#battery"/></svg></div>
  </div>
  <div class="brand" style="top:150px"><span class="brand-dot"></span>Parkovo</div>
  <div class="field" style="top:248px">E-mail</div>
  <div class="field" style="top:301px">Password</div>
  <div class="options-row">
    <span class="remember"><svg width="8" height="7"><path d="M1 3.5 L3.5 6 L7.5 1" stroke="var(--green)" stroke-width="1.3" fill="none"/></svg>Remember</span>
    <span class="forgot">Forget Password?</span>
  </div>
  <div class="btn" style="top:387px">SING IN</div>
  <div class="signup-line">Don't have Account?<strong>Create Account</strong></div>
  <div class="pager" style="top:523px"><span class="active"></span><span></span><span></span><span></span></div>
</section>

<!-- Reset password -->
<section class="screen" style="left:383px;top:24px">
  <div class="header"><svg width="307" height="74" viewBox="0 0 307 74"><use href="#wave"/></svg></div>
  <div class="status-bar">
    <svg class="signal" width="36" height="11"><use href="#status-signal"/></svg>
    <div class="time">10:30 AM</div>
    <div class="power"><svg width="8" height="12"><use href="#bluetooth"/></svg><span>100%</span><svg width="30" height="13"><use href="#battery"/></svg></div>
  </div>
  <div class="brand" style="top:150px"><span class="brand-dot"></span>Parkovo</div>
  <div class="field" style="top:248px">E-mail</div>
  <div class="choice choice--active" style="top:311px">
    <svg width="14" height="13"><rect x="0.5" y="1.5" width="11" height="11" fill="none" stroke="#bbb"/><path d="M2 6 L5.5 10 L13 1" stroke="var(--green)" stroke-width="1.8" fill="none"/></svg>
    Sent to the Email address
  </div>
  <div class="choice" style="top:343px"><span class="box"></span>Sent to the an SMS</div>
  <div class="btn btn--small" style="top:387px">SEND THE CODE</div>
  <div class="btn btn--small" style="top:435px">RESET THE PASSWORD</div>
  <div class="pager" style="top:523px"><span></span><span class="active"></span><span></span><span></span></div>
</section>

<!-- Register -->
<section class="screen" style="left:731px;top:21px">
  <div class="header"><svg width="307" height="74" viewBox="0 0 307 74"><use href="#wave"/></svg></div>
  <div class="status-bar">
    <svg class="signal" width="36" height="11"><use href="#status-signal"/></svg>
    <div class="time">10:30 AM</div>
    <div class="power"><svg width="8" height="12"><use href="#bluetooth"/></svg><span>100%</span><svg width="30" height="13"><use href="#battery"/></svg></div>
  </div>
  <div class="brand" style="top:150px"><span class="brand-dot"></span>Parkovo</div>
  <div class="field" style="top:248px">E-mail</div>
  <div class="field" style="top:300px">Password</div>
  <div class="field" style="top:352px">Cornfirm Password</div>
  <div class="field" style="top:405px">Phone Number</div>
  <div class="btn" style="top:469px">CORNFIRM</div>
  <div class="pager" style="top:522px"><span></span><span></span><span class="active"></span><span></span></div>
</section>

<!-- Register confirm -->
<section class="screen" style="left:39px;top:613px">
  <div class="header"><svg width="307" height="74" viewBox="0 0 307 74"><use href="#wave"/></svg></div>
  <div class="status-bar">
    <svg class="signal" width="36" height="11"><use href="#status-signal"/></svg>
    <div class="time">10:30 AM</div>
    <div class="power"><svg width="8" height="12"><use href="#bluetooth"/></svg><span>100%</span><svg width="30" height="13"><use href="#battery"/></svg></div>
  </div>
  <div class="brand" style="top:150px"><span class="brand-dot"></span>Parkovo</div>
  <div class="field" style="top:249px">E-mail</div>
  <div class="field" style="top:301px">Password</div>
  <div class="field" style="top:353px">Cornfirm Password</div>
  <div class="field" style="top:405px">Phone Number</div>
  <div class="btn" style="top:469px">CORNFIRM</div>
  <div class="pager" style="top:523px"><span></span><span></span><span></span><span class="active"></span></div>
</section>

<!-- Pay parking -->
<section class="screen" style="left:383px;top:613px">
  <div class="header header--tall">
    <svg width="307" height="112" viewBox="0 0 307 112">
      <rect x="0" y="0" width="307" height="40" fill="var(--green)"/>
      <use href="#wave" y="38"/>
    </svg>
  </div>
  <div class="status-bar">
    <svg class="signal" width="36" height="11"><use href="#status-signal"/></svg>
    <div class="time">10:30 AM</div>
    <div class="power"><svg width="8" height="12"><use href="#bluetooth"/></svg><span>100%</span><svg width="30" height="13"><use href="#battery"/></svg></div>
  </div>
  <svg class="menu-icon" width="26" height="22" viewBox="0 0 26 22" fill="#fff">
    <rect x="0" y="0" width="17" height="4" rx="2"/>
    <rect x="0" y="9" width="26" height="4" rx="2"/>
    <rect x="0" y="18" width="12" height="4" rx="2"/>
  </svg>
  <div class="page-title">Мапа</div>
  <div class="brand" style="top:185px"><span class="brand-dot"></span>Parkovo</div>
  <div class="field field--icon" style="top:250px">
    <svg width="14" height="17" viewBox="0 0 14 17"><path d="M7 0 C3 0 0 3 0 7 C0 11 7 17 7 17 C7 17 14 11 14 7 C14 3 11 0 7 0 Z" fill="var(--green)"/><circle cx="7" cy="7" r="2.6" fill="#fff"/></svg>
    Location
  </div>
  <div class="field field--icon" style="top:303px">
    <svg width="16" height="16" viewBox="0 0 16 16"><circle cx="8" cy="8" r="7" fill="none" stroke="var(--green)" stroke-width="1.6"/><path d="M8 4 V8 H11" stroke="var(--green)" stroke-width="1.6" fill="none"/></svg>
    Date
  </div>
  <div class="field field--indent" style="top:355px">Number Plate</div>
  <div class="btn btn--bold" style="top:422px">PAY PARKING</div>
  <nav class="tab-bar">
    <div class="tab tab--current">
      <svg width="22" height="16" viewBox="0 0 22 16" fill="#fff"><circle cx="7" cy="7" r="7"/><text x="7" y="10.5" font-size="10" font-weight="700" text-anchor="middle" fill="var(--green)" font-family="Roboto, sans-serif">$</text><rect x="11" y="6" width="11" height="7" rx="2"/><circle cx="13.5" cy="14" r="1.8"/><circle cx="19.5" cy="14" r="1.8"/></svg>
      PAY PARKING
    </div>
    <div class="tab">
      <svg width="24" height="16" viewBox="0 0 24 16"><rect x="0.5" y="0.5" width="23" height="15" rx="2" fill="#fff"/><circle cx="7" cy="6" r="2.5" fill="var(--green)"/><path d="M3 12 Q7 7 11 12 Z" fill="var(--green)"/><rect x="13" y="4" width="8" height="1.6" fill="var(--green)"/><rect x="13" y="8" width="8" height="1.6" fill="var(--green)"/></svg>
      USER CARD
    </div>
    <div class="tab">
      <svg width="20" height="17" viewBox="0 0 20 17"><path d="M10 0 L20 17 H0 Z" fill="#fff"/><rect x="9" y="5" width="2" height="7" fill="var(--green)"/><rect x="9" y="13.5" width="2" height="2" fill="var(--green)"/></svg>
      REPORT A PROBLEM
    </div>
  </nav>
</section>

</body>
</html>
```